Nexor Turbo Business Card Design

This is a start up company that has state of the art patented technology for turbo chargers,that can be used on engines, gas or diesel, for any type of automotive,aviation,marine or industrial purpose.
This technology will provide longer life,lower maintenance and better performance and help produce lower emissions with any turbocharged engine.Red would be a predominate color and the design should communicate the latest technology,economy and
Environmental concern.
This product will initially be distributed in the U.S.A. But should move rapidly to global use.
Updates

Thank you for your design submissions, I have increased the budget for this job because my initial order was too low for the quality of work shown, plus I would Like to see some more options. I have a meeting this Sunday with my other partners and would anticipate being able to give you some feedback by the Beginning of next week. Regards.

Thank you for everyone's participation. The deadline is still open until 6/15 and my partners and I have a meeting Scheduled this weekend. At this time we have not ruled anyone out, But will be making a decision during the course of our meeting and wil Decide which direction we will be going in by the beginning of the week. Thanks again, regards, Dan Ferris.

Hello everybody, Sorry for the delay in communication, we have been very busy in putting the start up together. We are still not decided on the design of the business card and have a wide range to choose from. I would anticipated we shall have an answer within the next two weeks. Regards, Dan Ferris.

Target Market(s)

Manufacturers and wholesalers' of OEM and replacement turbochargers

Industry/Entity Type

Industrial

Contact Information for Business Card

We need a logo that should incorporate the " Nexor, a " possibly super imposed over a turbo charger with the fan blades of the turbocharger showing in the center of the "a" .
Name,title,phone number and email address only, no street/mailing address at this time.
The full name of the company is
" Nexor Kinetic Systems LLC "
For the initial card you can use my info.
Daniel Ferris
VP Sales & Marketing
dferris@nexorkineticsystems.com
555 014 2876

Requirements
Must have
• The Nexor A, the outline of a turbo charger
Nice to have
• Something classy and simple and worldly (global)
Should not have
• No engines,cars,boats,planes

```html
<!DOCTYPE html>
<html lang="en">
<head>
<meta charset="utf-8">
<title>Nexor Kinetic Systems LLC — Business Card</title>
<link rel="stylesheet" href="https://fonts.googleapis.com/css2?family=Oswald:wght@600&family=Open+Sans:wght@400&display=swap">
<style>
  :root {
    --backdrop: #ffb8ae;
    --brand-red: #ee3124;
    --card-white: #ffffff;
    --ink: #1d1d1d;
    --title-font: "Oswald", "Arial Narrow", sans-serif;
    --body-font: "Open Sans", Arial, sans-serif;
  }
  * { box-sizing: border-box; margin: 0; padding: 0; }
  html, body {
    width: 1200px; height: 900px; overflow: hidden;
    background: var(--backdrop);
  }
  .business-card {
    position: absolute; left: 180px; top: 210px;
    width: 840px; height: 480px;
    background: var(--card-white);
    box-shadow: 0 10px 30px rgba(120, 40, 30, 0.25);
    overflow: hidden;
  }
  .brand-band {
    position: absolute; left: 0; top: 0; right: 0; height: 240px;
    background: var(--brand-red);
    display: flex; align-items: center;
    padding: 0 56px;
    gap: 34px;
  }
  .brand-dot {
    width: 128px; height: 128px; border-radius: 50%;
    background: var(--card-white); flex: none;
  }
  .company-name {
    font-family: var(--title-font); font-weight: 600;
    color: var(--card-white);
    font-size: 62px; line-height: 1.02;
    text-transform: uppercase; letter-spacing: 0.5px;
  }
  .contact-list {
    position: absolute; right: 60px; top: 272px;
    list-style: none;
    font-family: var(--body-font); font-size: 21px; color: var(--ink);
  }
  .contact-list li {
    display: flex; align-items: center; gap: 12px; margin-bottom: 6px;
  }
  .contact-icon { width: 22px; height: 22px; flex: none; }
  .person {
    position: absolute; left: 56px; bottom: 70px;
    font-family: var(--body-font);
  }
  .person-name {
    font-size: 25px; color: var(--ink); text-transform: uppercase; letter-spacing: 0.5px;
  }
  .person-title { font-size: 21px; color: var(--brand-red); }
  .accent-rule {
    position: absolute; left: 0; right: 0; bottom: 40px;
    height: 2px; background: var(--brand-red);
  }
</style>
</head>
<body>
  <article class="business-card">
    <header class="brand-band">
      <div class="brand-dot" aria-hidden="true"></div>
      <h1 class="company-name">Nexor Kinetic<br>Systems LLC</h1>
    </header>

    <ul class="contact-list">
      <li>
        <svg class="contact-icon" viewBox="0 0 22 22" aria-hidden="true">
          <circle cx="11" cy="11" r="11" fill="var(--brand-red)"/>
          <path d="M7.5 6h2l1 2.6-1.3 1a6 6 0 0 0 3.2 3.2l1-1.3 2.6 1v2a1 1 0 0 1-1 1A9 9 0 0 1 6.5 7a1 1 0 0 1 1-1z" fill="#fff"/>
        </svg>
        <span>555 014 2876</span>
      </li>
      <li>
        <svg class="contact-icon" viewBox="0 0 22 22" aria-hidden="true">
          <circle cx="11" cy="11" r="11" fill="var(--brand-red)"/>
          <rect x="5.5" y="7" width="11" height="8" rx="1" fill="#fff"/>
          <path d="M5.8 7.4 11 11.4l5.2-4" fill="none" stroke="var(--brand-red)" stroke-width="1.2"/>
        </svg>
        <span>dferris@nexorkineticsystems.com</span>
      </li>
    </ul>

    <div class="person">
      <p class="person-name">Daniel Ferris</p>
      <p class="person-title">VP Sales &amp; Marketing</p>
    </div>

    <div class="accent-rule" aria-hidden="true"></div>
  </article>
</body>
</html>
```